Business Cards

I am a landscape designer and I am hired to do over the top landscapes!
I pay attention to detail and do everything from growing my own orchids and Fruits and Vegetables.
I build ponds water features. I do Landscape Lighting and Specialize in Drip Irrigation for New Landscapes.
I am looking for something with a picture of one of my landscapes and pictures of Orchids on the back so I can work on growing my Orchid business.
I like the plastic cards.
I like Saturation
I like color and I want something that really sticks out!
I will attach a few pics!
Thanks
Corey
A Bright Terrace LLC
Corey Valdrup
Orchids & Organic Farming
Landscaping Made Simple
555-204-7193
Abrightterrace@mailnest.example
Coral Vista Bay FL

Target Market(s)

I work for Wealthy Clients who want unique designs and enjoy rare plants.
I am the goto guy for tropical and rare plants
Cool Designs
Orchids
Interior Decorating
Exterior Lighting
Organic Farming
People who appreciate plants

Industry/Entity Type

Landscape

Font styles to use
Decorative

Requirements
Must have
• COLOR COLOR COLOR
Saturation
Sleek and Clean
Should not have
• tacky

```html
<!DOCTYPE html>
<html lang="en">
<head>
<meta charset="utf-8">
<title>A Bright Terrace LLC – Business Cards</title>
<link rel="stylesheet" href="https://fonts.googleapis.com/css2?family=Cinzel:wght@500&family=Cormorant+Garamond:ital,wght@1,600&family=Arimo&display=swap">
<style>
  :root {
    --page: #ffffff;
    --card-green: #2e8a55;
    --card-green-deep: #257348;
    --brand-yellow: #f3e41d;
    --crescent-yellow: #f6ec1a;
    --frame-orange: #f08a1c;
    --tagline: #eef2dc;
    --contact: #ffffff;
    --garden-light: #9bcf5a;
    --garden-dark: #3d6b2a;
    --orchid-magenta: #b1357a;
    --orchid-soft: #d9b7c6;
    --orchid-violet: #7a3fb8;
    --orchid-deep: #5a2a8e;
  }
  * { box-sizing: border-box; margin: 0; padding: 0; }
  html, body { width: 1200px; height: 900px; overflow: hidden; background: var(--page); }
  .canvas { position: relative; width: 1200px; height: 900px; }
  .card {
    position: absolute; top: 290px; width: 560px; height: 320px;
    border-radius: 18px; overflow: hidden;
    background: radial-gradient(circle at 40% 45%, var(--card-green) 0%, var(--card-green-deep) 100%);
    box-shadow: 0 10px 24px rgba(0,0,0,0.18);
  }
  .card--front { left: 30px; }
  .card--back { left: 610px; }
  .card-art { position: absolute; inset: 0; }

  .brand {
    font-family: "Cinzel", serif; font-weight: 500;
    color: var(--brand-yellow); text-align: center; line-height: 1.05;
  }
  .card--front .brand { position: absolute; left: 14px; top: 30px; width: 250px; font-size: 29px; }
  .card--back .brand { position: absolute; left: 195px; top: 224px; width: 200px; font-size: 21px; }

  .tagline {
    position: absolute; left: 14px; top: 112px; width: 250px; text-align: center;
    font-family: "Cormorant Garamond", serif; font-style: italic; font-weight: 600;
    font-size: 17px; line-height: 1.3; color: var(--tagline);
  }
  .person {
    position: absolute; left: 30px; top: 178px;
    font-family: "Cormorant Garamond", serif; font-style: italic; font-weight: 600;
    font-size: 24px; color: var(--brand-yellow);
  }
  .contact-list {
    position: absolute; left: 30px; top: 222px; list-style: none;
    font-family: "Arimo", sans-serif; font-size: 13px; color: var(--contact); line-height: 22px;
  }
  .contact-list li { display: flex; align-items: center; gap: 7px; white-space: nowrap; }
  .contact-icon { width: 13px; height: 13px; flex: none; fill: var(--brand-yellow); }
</style>
</head>
<body>
<main class="canvas">

  <section class="card card--front" aria-label="Business card front">
    <svg class="card-art" viewBox="0 0 560 320" width="560" height="320">
      <path d="M262 0 C232 100 240 230 300 320 L322 320 C272 230 262 100 292 0 Z" fill="var(--crescent-yellow)"/>
      <defs>
        <linearGradient id="garden" x1="0" y1="0" x2="0.4" y2="1">
          <stop offset="0" stop-color="var(--garden-light)"/>
          <stop offset="0.55" stop-color="var(--garden-dark)"/>
          <stop offset="1" stop-color="#8e8a86"/>
        </linearGradient>
      </defs>
      <path role="img" aria-label="Photo of a lush tropical landscaped garden with palms, red bromeliads and river-stone paths"
            d="M292 0 C262 100 272 230 322 320 L560 320 L560 0 Z" fill="url(#garden)"/>
    </svg>
    <div class="brand">A Bright<br>Terrace LLC</div>
    <p class="tagline">Orchids &amp; Organic Growing<br>Gardens Made Effortless</p>
    <p class="person">Corey Valdrup</p>
    <ul class="contact-list">
      <li><svg class="contact-icon" viewBox="0 0 24 24"><path d="M6.6 10.8a15 15 0 0 0 6.6 6.6l2.2-2.2a1 1 0 0 1 1-.25 11.4 11.4 0 0 0 3.6.57 1 1 0 0 1 1 1V20a1 1 0 0 1-1 1A17 17 0 0 1 3 4a1 1 0 0 1 1-1h3.5a1 1 0 0 1 1 1c0 1.25.2 2.45.57 3.6a1 1 0 0 1-.25 1z"/></svg>555-204-7193</li>
      <li><svg class="contact-icon" viewBox="0 0 24 24"><path d="M2 5h20v14H2z M2 5l10 8 10-8" fill="var(--brand-yellow)" stroke="var(--card-green)" stroke-width="1.5"/></svg>Abrightterrace@mailnest.example</li>
      <li><svg class="contact-icon" viewBox="0 0 24 24"><path d="M12 3 2 12h3v9h5v-6h4v6h5v-9h3z"/></svg>Coral Vista Bay FL</li>
    </ul>
  </section>

  <section class="card card--back" aria-label="Business card back">
    <svg class="card-art" viewBox="0 0 560 320" width="560" height="320">
      <defs>
        <linearGradient id="orchid-left" x1="0" y1="0" x2="1" y2="1">
          <stop offset="0" stop-color="var(--orchid-soft)"/>
          <stop offset="0.5" stop-color="var(--orchid-magenta)"/>
          <stop offset="1" stop-color="#9c8f86"/>
        </linearGradient>
        <linearGradient id="orchid-right" x1="0" y1="0" x2="1" y2="1">
          <stop offset="0" stop-color="var(--orchid-violet)"/>
          <stop offset="1" stop-color="var(--orchid-deep)"/>
        </linearGradient>
      </defs>
      <path role="img" aria-label="Photo of white and magenta spotted orchid blooms"
            d="M0 0 L200 0 C242 100 236 230 188 320 L0 320 Z" fill="url(#orchid-left)"
            stroke="var(--frame-orange)" stroke-width="4"/>
      <path role="img" aria-label="Photo of deep violet orchid blooms"
            d="M402 0 C366 100 362 220 386 320 L560 320 L560 0 Z" fill="url(#orchid-right)"
            stroke="var(--frame-orange)" stroke-width="4"/>
    </svg>
    <div class="brand">A Bright<br>Terrace LLC</div>
  </section>

</main>
</body>
</html>
```